Charged by courts for driving with suspended license

To be seen by judges and lawyers. Would like some consistency between the brochures which is why we have used same images in places.

Target Market(s)

Lawyers, judges

Industry/Entity Type

legal, auto

Font styles to use
Sans Serif

Requirements
Nice to have
• I like the gears graphic I have used, but open to other ideas. Should be less industrial/automotive rather reflect mentally Turning Point as clients need to change driving behaviour
Should not have
• images with manufacturers names etc. Maybe not have bright colours that are fun or summery as this si for judges, legal profession and must be serious, professional and stately

```html
<!DOCTYPE html>
<html lang="en">
<head>
<meta charset="utf-8">
<title>Turning Point – Trifold Brochure</title>
<link rel="stylesheet" href="https://fonts.googleapis.com/css2?family=Montserrat:ital,wght@0,400;0,800;0,900;1,300;1,400&family=Oswald:wght@300;400;500&family=Roboto:wght@400;700&display=swap">
<style>
:root{
  --stage:#e6e6e6;
  --paper:#f2f2f2;
  --paper-shade:#dcdcdc;
  --ink:#1b1b1b;
  --ink-soft:#3a3a3a;
  --night:#151515;
  --bronze:#6e4b14;
  --brand:#1f4a96;
  --white:#ffffff;
}
*{box-sizing:border-box;margin:0;padding:0}
html,body{width:1200px;height:1000px;overflow:hidden;background:var(--stage)}
.canvas{position:relative;width:1200px;height:1000px}
.spread{position:absolute;left:30px;width:1140px;height:470px;display:flex;box-shadow:0 6px 18px rgba(0,0,0,.18)}
.spread--inside{top:18px}
.spread--outside{top:512px}
.panel{position:relative;width:380px;height:470px;overflow:hidden;background:linear-gradient(180deg,var(--paper),var(--paper-shade))}
.panel + .panel{border-left:1px solid #cfcfcf}
.panel__body{position:relative;padding:20px 24px;font-family:'Roboto',sans-serif;font-size:9.6px;line-height:1.28;color:var(--ink)}

.kicker{font-family:'Oswald',sans-serif;font-weight:300;letter-spacing:3px;font-size:15px;line-height:1}
.title-main{font-family:'Montserrat',sans-serif;font-weight:900;text-transform:uppercase;color:var(--ink);letter-spacing:-.5px;line-height:.9}
.title-main--small{font-size:21px;margin-bottom:8px}
.lead{font-weight:700;font-size:11px;margin-bottom:6px}
.section-head{font-weight:700;margin:8px 0 2px}
.roman{list-style:upper-roman;padding-left:22px}
.roman li{padding-left:4px;text-align:justify}

.image-slot{position:absolute}
.head-profile-light{left:0;top:0;width:100%;height:100%;background:radial-gradient(ellipse at 80% 45%,#ffffff 0%,#ececec 35%,#bdbdbd 70%,#9a9a9a 100%)}
.course-art{left:60px;top:256px;width:170px;height:130px;border-radius:8px;background:linear-gradient(135deg,#d6dbe4,#9aa6bb)}

.promo{position:absolute;right:20px;text-align:right;font-family:'Montserrat',sans-serif;color:var(--ink)}
.promo__one{top:30px;font-weight:800;font-size:21px;line-height:1.05}
.promo__title{top:92px;font-weight:900;font-size:44px;line-height:.86;text-transform:uppercase;text-shadow:2px 2px 0 #bbb}
.promo__remote{top:196px;font-family:'Oswald',sans-serif;font-weight:500;font-size:22px;line-height:1.05;color:var(--bronze)}
.remote-icon{position:absolute;left:60px;top:196px}
.price{position:absolute;left:60px;top:396px;display:flex;align-items:center;gap:6px;font-family:'Montserrat',sans-serif;font-weight:800;font-size:13px;color:var(--ink)}
.price__tag{background:var(--night);color:var(--white);font-size:8px;padding:3px 5px}

.brand{position:absolute;display:flex;align-items:center;gap:7px;font-family:'Montserrat',sans-serif;font-weight:800;color:var(--brand)}
.brand__dot{width:16px;height:16px;border-radius:50%;background:var(--brand)}
.brand--inside{right:20px;bottom:18px;font-size:22px}
.brand--cover{left:26px;bottom:26px;font-size:26px}

.background{padding:24px 26px}
.background h2{font-family:'Roboto',sans-serif;font-size:16px;margin-bottom:10px}
.background p{font-size:9.6px;text-align:justify;margin-bottom:9px}

.back{background:linear-gradient(180deg,#262626,var(--night));color:var(--white);text-align:center}
.back__motto{position:absolute;top:60px;left:30px;right:30px;font-family:'Montserrat',sans-serif;font-style:italic;font-weight:300;font-variant:small-caps;font-size:22px;line-height:1.75;letter-spacing:1px}
.back__contact{position:absolute;bottom:26px;left:0;right:0;font-family:'Roboto',sans-serif}
.back__label{font-weight:700;font-size:11px;margin-bottom:8px}
.back__phone{display:flex;justify-content:center;align-items:center;gap:8px;font-weight:700;font-size:17px;margin-bottom:8px}
.back__web{font-family:'Georgia',serif;font-size:11px;line-height:1.6}

.cover .head-profile-dark{right:0;top:0;width:55%;height:100%;background:linear-gradient(90deg,rgba(60,60,60,0) 0%,#5a5a5a 40%,#2a2a2a 100%)}
.cover__title{position:absolute;left:26px;top:28px;font-size:40px;text-shadow:2px 2px 0 #fff,3px 3px 0 #999}
.cover__subtitle{position:absolute;left:26px;top:148px;font-family:'Oswald',sans-serif;text-transform:uppercase;color:var(--ink);line-height:1.05}
.cover__subtitle .big{font-size:30px;font-weight:500}
.cover__subtitle .mid{font-size:17px;font-weight:400;display:block}
.cover__audience{position:absolute;left:26px;top:292px;font-family:'Oswald',sans-serif;text-transform:uppercase;color:var(--ink);line-height:1.35}
.cover__audience .sm{font-size:9px;font-weight:300;display:block}
.cover__audience .md{font-size:13px;display:block}
</style>
</head>
<body>
<main class="canvas">

  <section class="spread spread--inside" aria-label="Brochure inside">
    <article class="panel">
      <div class="panel__body">
        <p class="kicker">SUSPENDED LICENCE -</p>
        <h1 class="title-main title-main--small">Turning Point</h1>
        <p class="lead">During The Course We Will:</p>
        <p class="section-head">Defensive Driving Module (The Big 4):</p>
        <ol class="roman">
          <li>Lane position (better to drop 2 wheels on the shoulder than hit an oncoming vehicle)</li>
          <li>Following distance (varies depending on speed and conditions); space cushion driving (always have an out)</li>
          <li>Defensive stopping (what should we do every time we apply brakes?)</li>
          <li>Strategic driving / what we do with our eyes:</li>
        </ol>
        <p class="section-head">Law:</p>
        <ol class="roman">
          <li>Highway Traffic Act (privilege vs right); Federal &amp; Provincial; ways we can lose our license</li>
          <li>Implications of a criminal record (relationships, work, financial)</li>
        </ol>
        <p class="section-head">Road Rage:</p>
        <ol class="roman">
          <li>Defining the continuum of road rage and escalation of anger</li>
          <li>Triggers</li>
          <li>Personality types (Type A); Holmes &amp; Rahe stress scale</li>
          <li>Aggressive driving (overlap between aggressors and victims); reframing our views</li>
          <li>Psychiatric issues/PTSD: Not uncommon to have professional drivers come through the course due to over-exposure to stress from driving (both on the job and/or the commute to their driving job)</li>
        </ol>
      </div>
    </article>

    <article class="panel">
      <div class="panel__body">
        <p class="section-head">Physiology of Aggressive Driving and How It Affects The Body:</p>
        <ol class="roman">
          <li>Window of tolerance (hyper-arousal vs hypo-arousal)</li>
          <li>Fight or flight response: how it works</li>
          <li>Stress hormones (Adrenaline, Cortisol, Norepinephrine)</li>
          <li>Chronic levels of exposure/Immune system suppression</li>
          <li>Hypertension</li>
          <li>Sympathetic nervous system</li>
          <li>Substances - will do an overview of alcohol/drinking and driving if relevant; individual and general factors that contribute to B.A.C</li>
        </ol>
        <p class="section-head">Personal Context (Risk Vs Protective Factors); Incumbent Upon Us to Consider:</p>
        <ol class="roman">
          <li>Genetics (chemical predispositions)</li>
          <li>Socialization (role models)</li>
          <li>Environment</li>
        </ol>
        <p class="section-head">Strategies to Manage:</p>
        <ol class="roman">
          <li>Stages of change theory; habit formation and how to reprogram (many of our decisions on any day are subconscious i.e., no decision-making process)</li>
          <li>Neuroplasticity and habit formation</li>
          <li>Supernormal stimuli: how our bodies have not kept up to the complexities of today's society and its stresses</li>
          <li>Ensure cerebral part of brain is making decisions and not "lizard" part of brain (amygdala vs cerebrum and their roles in the body); triggers &amp; stressors</li>
        </ol>
      </div>
    </article>

    <article class="panel">
      <div class="image-slot head-profile-light" role="img" aria-label="Side profile silhouette of a head facing left in soft grey tones"></div>
      <p class="promo promo__one">COURSES ARE<br>ONE-ON-ONE</p>
      <h2 class="promo promo__title">Turning<br>Point</h2>
      <svg class="remote-icon" width="44" height="44" viewBox="0 0 44 44" aria-hidden="true">
        <rect x="3" y="10" width="30" height="22" rx="2" fill="none" stroke="#1b1b1b" stroke-width="3"/>
        <rect x="14" y="34" width="8" height="4" fill="#1b1b1b"/>
        <rect x="24" y="2" width="18" height="13" rx="3" fill="#6e4b14"/>
      </svg>
      <p class="promo promo__remote">OFFERED<br>REMOTELY!</p>
      <div class="image-slot course-art" role="img" aria-label="Illustration of remote online learning with an instructor and screens"></div>
      <p class="price"><span class="price__tag">Course Cost:</span>$775.00 + HST</p>
      <p class="brand brand--inside"><span class="brand__dot"></span>Lanewise</p>
    </article>
  </section>

  <section class="spread spread--outside" aria-label="Brochure outside">
    <article class="panel">
      <div class="panel__body background">
        <h2>Our Background:</h2>
        <p>Since its inception in 1998, <b>Lanewise Driving School</b> has strived to help drivers maintain their driving independence while leading safe and productive lives. Our motto <i>"steady habits for every road"</i> drives our vision of helping drivers across industries and at all stages of our driving careers.</p>
        <p><b>Lanewise</b> started out working with school boards to deliver driver training to beginner drivers. Thousands of students have graduated from our ministry-approved curriculum. We are also ministry-approved to instruct defensive driving (DDC) and driver improvement courses (DIC), for drivers with speeding tickets, demerit points and at fault crashes.</p>
        <p><b>Lanewise</b> has also evolved to provide comprehensive driver rehabilitation to those who have lost, or are at risk of losing their license for medical reasons. This includes mobility issues requiring adaptive equipment, as well as traumatic crashes resulting in cognitive impairments and PTSD. We work with clients before the courts charged with impaired driving (alcohol, cannabis, opioids), road rage and stunt driving.</p>
        <p>Founder Daniel Hale started driving at an early age on his parent's farm. Driving professionally and doing so safely is in his DNA. Daniel has a degree in Business and Psychology from Lakeshore University and is a certified in-car and in-class driving instructor.</p>
      </div>
    </article>

    <article class="panel back">
      <p class="back__motto">Maintaining driving independence, while leading safe and productive lives!</p>
      <div class="back__contact">
        <p class="back__label">For more information:</p>
        <p class="back__phone">
          <svg width="20" height="20" viewBox="0 0 24 24" aria-hidden="true"><path fill="#fff" d="M6.6 10.8c1.4 2.8 3.8 5.1 6.6 6.6l2.2-2.2c.3-.3.7-.4 1-.2 1.1.4 2.3.6 3.6.6.6 0 1 .4 1 1V20c0 .6-.4 1-1 1C10.6 21 3 13.4 3 4c0-.6.4-1 1-1h3.5c.6 0 1 .4 1 1 0 1.3.2 2.5.6 3.6.1.3 0 .7-.2 1L6.6 10.8z"/></svg>
          705-555-0184
        </p>
        <p class="back__web">www.lanewisedriving.ca<br>dhale@lanewisedriving.ca</p>
      </div>
    </article>

    <article class="panel cover">
      <div class="image-slot head-profile-dark" role="img" aria-label="Dark grey head silhouette filled with interlocking gears"></div>
      <h1 class="title-main cover__title">Turning<br>Point</h1>
      <p class="cover__subtitle"><span class="big">A 1-Day</span><span class="mid">Educational</span><span class="mid">Course</span></p>
      <p class="cover__audience"><span class="sm">For those</span><span class="sm">charged with</span><span class="md">Driving on</span><span class="md">a suspended</span><span class="md">licence</span></p>
      <p class="brand brand--cover"><span class="brand__dot"></span>Lanewise</p>
    </article>
  </section>

</main>
</body>
</html>
```